Bref créative
Business Stationery
Corvane Vantage
Professional
Belinda Hawthorpe
Managing Director
Lagos - Dublin - London
bel@corvanevantage.com
www.corvanevantage.com
Quorn Logo
logo vector file

```html
<!DOCTYPE html>
<html lang="en">
<head>
<meta charset="utf-8">
<title>Corvane Vantage — Business Stationery</title>
<link rel="stylesheet" href="https://fonts.googleapis.com/css2?family=Questrial&family=Arimo:wght@400;700&display=swap">
<style>
  :root {
    --backdrop-dark: #111214;
    --backdrop-mid: #2a2c30;
    --card-white: #ffffff;
    --ink: #3b3b3b;
    --green-deep: #2f7d12;
    --green: #5aa51c;
    --green-light: #a6d64a;
    --band-dark: #1d1d1d;
  }
  * { margin: 0; padding: 0; box-sizing: border-box; }
  html, body { width: 1200px; height: 557px; overflow: hidden; }
  body {
    position: relative;
    background: radial-gradient(ellipse at 50% 45%, var(--backdrop-mid) 0%, var(--backdrop-dark) 75%);
    font-family: "Arimo", Arial, sans-serif;
    color: var(--ink);
  }
  .card {
    position: absolute;
    width: 314px;
    height: 212px;
    background: var(--card-white);
    box-shadow: 0 4px 10px rgba(0,0,0,.6);
    overflow: hidden;
  }
  .card--front-detail { left: 236px; top: 72px; width: 320px; }
  .card--back-mark    { left: 590px; top: 72px; }
  .card--compact      { left: 100px; top: 296px; }
  .card--wordmark     { left: 424px; top: 296px; }
  .card--green        { left: 748px; top: 296px; }

  .brand {
    font-family: "Questrial", "Century Gothic", sans-serif;
    color: var(--ink);
    white-space: nowrap;
  }
  .brand-dot {
    display: block;
    border-radius: 50%;
    background: radial-gradient(circle at 35% 35%, var(--green-light), var(--green-deep));
  }
  .web {
    position: absolute;
    left: 0; right: 0;
    text-align: center;
    font-size: 10px;
    letter-spacing: 1.6px;
    color: var(--ink);
  }

  /* front with contact band */
  .card--front-detail .brand-dot { position: absolute; left: 144px; top: 18px; width: 32px; height: 32px; }
  .card--front-detail .brand { position: absolute; left: 0; right: 0; top: 56px; text-align: center; font-size: 19px; }
  .person { position: absolute; left: 0; right: 0; top: 90px; text-align: center; font-size: 10px; color: var(--ink); }
  .person .role { color: var(--green); font-size: 9px; }
  .contact-band {
    position: absolute; left: 0; right: 0; bottom: 0; height: 62px;
    background: linear-gradient(100deg, var(--band-dark) 0%, var(--band-dark) 52%, var(--green-deep) 70%, var(--green-light) 100%);
    color: #f2f2f2; font-size: 7.5px;
    display: grid; grid-template-columns: 1fr 1fr 1.15fr; align-content: center; row-gap: 8px;
    padding: 0 10px;
  }
  .contact-band span { display: flex; align-items: center; gap: 4px; white-space: nowrap; }
  .contact-band svg { width: 8px; height: 8px; flex: none; }
  .contact-band .cities { grid-column: 2 / 4; }

  /* back with mark */
  .card--back-mark .brand-dot { position: absolute; left: 131px; top: 38px; width: 52px; height: 52px; }
  .card--back-mark .brand { position: absolute; left: 0; right: 0; top: 100px; text-align: center; font-size: 17px; }
  .card--back-mark .web { top: 150px; }

  /* compact logo card */
  .card--compact .brand-dot { position: absolute; left: 141px; top: 34px; width: 32px; height: 32px; }
  .card--compact .brand { position: absolute; left: 0; right: 0; top: 78px; text-align: center; font-size: 21px; }
  .card--compact .web { top: 162px; }

  /* wordmark card */
  .card--wordmark { background: linear-gradient(180deg, #ffffff 0%, #eef5e6 100%); }
  .card--wordmark .brand { position: absolute; left: 0; right: 0; top: 74px; text-align: center; font-size: 32px; }
  .card--wordmark .web { top: 166px; }

  /* green card */
  .card--green { background: linear-gradient(135deg, var(--green-light) 0%, var(--green) 40%, var(--green-deep) 100%); }
  .glow-band {
    position: absolute; left: 14px; right: 14px; top: 66px; height: 58px;
    background: radial-gradient(ellipse at center, rgba(255,255,255,.95) 0%, rgba(255,255,255,.75) 45%, rgba(255,255,255,0) 75%);
  }
  .card--green .brand { position: absolute; left: 0; right: 0; top: 76px; text-align: center; font-size: 32px; }
  .card--green .web { top: 166px; color: #ffffff; }
</style>
</head>
<body>

  <section class="card card--front-detail" aria-label="Business card front">
    <span class="brand-dot"></span>
    <div class="brand">Corvane Vantage</div>
    <p class="person"><strong>Belinda Hawthorpe</strong>, <span class="role">Managing Director</span></p>
    <div class="contact-band">
      <span><svg viewBox="0 0 10 10"><path d="M2 1l2 2-1 1.3c.6 1.2 1.5 2.1 2.7 2.7L7 6l2 2-1.5 1.5C4.5 9 1 5.5.5 2.5z" fill="#fff"/></svg>020 7946 0183</span>
      <span><svg viewBox="0 0 10 10"><path d="M2 1l2 2-1 1.3c.6 1.2 1.5 2.1 2.7 2.7L7 6l2 2-1.5 1.5C4.5 9 1 5.5.5 2.5z" fill="#fff"/></svg>0161 496 0752</span>
      <span><svg viewBox="0 0 10 10"><rect x="1" y="2" width="8" height="6" fill="none" stroke="#fff"/><path d="M1 2l4 3 4-3" fill="none" stroke="#fff"/></svg>bel@corvanevantage.com</span>
      <span><svg viewBox="0 0 10 10"><circle cx="5" cy="5" r="4" fill="none" stroke="#fff"/><path d="M1 5h8M5 1c2 2 2 6 0 8M5 1c-2 2-2 6 0 8" fill="none" stroke="#fff" stroke-width=".7"/></svg>www.corvanevantage.com</span>
      <span class="cities"><svg viewBox="0 0 10 10"><path d="M5 9.5S1.8 6 1.8 3.8a3.2 3.2 0 016.4 0C8.2 6 5 9.5 5 9.5z" fill="#fff"/><circle cx="5" cy="3.8" r="1.2" fill="#2f7d12"/></svg>Lagos - Dublin - London</span>
    </div>
  </section>

  <section class="card card--back-mark" aria-label="Business card back">
    <span class="brand-dot"></span>
    <div class="brand">Corvane Vantage</div>
    <p class="web">www.corvanevantage.com</p>
  </section>

  <section class="card card--compact" aria-label="Business card back, alternate">
    <span class="brand-dot"></span>
    <div class="brand">Corvane Vantage</div>
    <p class="web">www.corvanevantage.com</p>
  </section>

  <section class="card card--wordmark" aria-label="Business card, wordmark variant">
    <div class="brand">Corvane Vantage</div>
    <p class="web">www.corvanevantage.com</p>
  </section>

  <section class="card card--green" aria-label="Business card, green variant">
    <div class="glow-band"></div>
    <div class="brand">Corvane Vantage</div>
    <p class="web">www.corvanevantage.com</p>
  </section>

</body>
</html>
```